Speisekarten-Design für Biergarten am Ufer des Bodensees
Super tolle Designerin. Vielen Dank Roswitha!
Zielgruppe
Wir sind ein direkt am Ufer des Bodensees liegender Biergarten, welcher seit über 30 Jahren besteht und deshalb fest in unserer Stadt verwurzelt ist. Zu unserer Zielgruppe gehören Touristen und Einheimische jeglicher Art - wir heißen einfach alle willkommen. Wir bieten unseren Gästen einfache Speisen und lokale Getränke. Uns ist wichtig, dass die Speise- & Getränkekarte das Gefühl von Heimat, Regionalität und Liebe zum Bodensee vermittelt. Wir bevorzugen ein modernes und klares Design, welches jedoch klassische Strukturen wie die eines typischen 60er-Jahre-Diners miteinbezieht.
Aufgabenstellung
Es wäre es toll, wenn diese Faltbar und kompakt (DIN-A4 evtl. etwas größer) ist. Die Textfelder sollten das komplette Speise- und Getränkeangebot darstellen (ca. 15 Gerichte, 6 Biersorten, 6 Softdrinks, 6 Heißgetränke). Wir bevorzugen warme Farbtöne. Es ist nicht notwendig Bilder in der Karte zu hinterlegen.

```html
<!DOCTYPE html>
<html lang="de">
<head>
<meta charset="utf-8">
<title>Speisekarte Biergarten am Bodensee</title>
<link rel="stylesheet" href="https://fonts.googleapis.com/css2?family=Alegreya+Sans:wght@300;400;500;700&family=Alegreya+Sans+SC:wght@700&family=Caveat:wght@500&display=swap">
<style>
  :root {
    --stage: #d4d3d7;
    --paper: #ffe57c;
    --paper-deep: #ffd863;
    --orange: #f39a1d;
    --orange-light: #f7b23a;
    --orange-dark: #d7802c;
    --box: rgba(246, 170, 52, 0.45);
    --box-tab: rgba(244, 160, 40, 0.6);
    --map: 217, 191, 140;
    --ink: #2a2430;
    --ink-soft: #4b3f3a;
    --detail: #8a3b12;
    --rule: rgba(150, 80, 20, 0.35);
  }
  * { margin: 0; padding: 0; box-sizing: border-box; }
  html, body { width: 1200px; height: 800px; overflow: hidden; }
  body { background: var(--stage); font-family: "Alegreya Sans", sans-serif; color: var(--ink); }
  .canvas { position: relative; width: 1200px; height: 800px; }

  .spread {
    position: absolute; top: 30px; width: 520px; height: 740px; overflow: hidden;
    background: linear-gradient(170deg, var(--paper) 0%, var(--paper) 60%, var(--paper-deep) 80%, var(--orange-light) 100%);
    box-shadow: 0 8px 24px rgba(0,0,0,0.18);
  }
  .spread--outer { left: 50px; }
  .spread--inner { left: 630px; }
  .fold { position: absolute; left: 260px; top: 0; bottom: 0; width: 1px; background: rgba(180, 110, 40, 0.35); }
  .waves { position: absolute; left: 0; width: 100%; }
  .waves--top { top: 0; height: 120px; }
  .waves--bottom { bottom: 0; height: 90px; }

  .panel { position: absolute; top: 0; width: 260px; height: 100%; }
  .panel--left { left: 0; }
  .panel--right { left: 260px; }

  .lake-map {
    position: absolute; left: 0; top: 40px; width: 520px; height: 310px;
    background: radial-gradient(ellipse 65% 60% at 55% 45%, rgba(var(--map), 0.75) 0%, rgba(var(--map), 0.45) 55%, rgba(var(--map), 0) 100%);
  }

  .section-tab {
    position: absolute; height: 30px; background: var(--box-tab); border-radius: 8px;
    font-family: "Alegreya Sans SC", sans-serif; font-weight: 700; font-size: 17px;
    color: var(--ink); display: flex; align-items: center; padding: 0 22px;
  }
  .section-tab--right { justify-content: flex-end; }
  .menu-box { position: absolute; background: var(--box); border-radius: 10px; padding: 14px 12px 10px 8px; }

  .menu-item { display: grid; grid-template-columns: 22px 1fr; margin-bottom: 4px; padding-bottom: 3px; }
  .menu-item + .menu-item { border-top: 1px solid var(--rule); padding-top: 3px; }
  .menu-item__no { font-size: 11px; color: var(--ink-soft); padding-top: 2px; }
  .menu-item__line { display: flex; align-items: baseline; font-size: 13px; font-weight: 400; }
  .menu-item__dots { flex: 1; border-bottom: 1.5px dotted var(--ink-soft); margin: 0 2px; transform: translateY(-3px); }
  .menu-item__price { font-size: 12px; }
  .menu-item__detail { grid-column: 2; font-size: 10px; color: var(--detail); line-height: 1.1; }
  .menu-item__detail sup { font-size: 6px; }

  .menu-box--dishes .menu-item { margin-bottom: 2px; }
  .menu-box--dishes .menu-item__line { font-size: 12.5px; }

  .hours { position: absolute; left: 0; width: 260px; top: 458px; text-align: center; color: var(--ink-soft); font-size: 11px; line-height: 1.15; }
  .hours__title { font-size: 13px; color: var(--ink); }
  .hours__note { font-size: 7.5px; margin-bottom: 10px; }
  .hours__block { margin-bottom: 8px; }
  .hours__day { color: var(--ink); }

  .fine-print { position: absolute; left: 12px; width: 236px; top: 602px; text-align: center; font-size: 5.2px; line-height: 1.35; color: var(--ink-soft); }
  .fine-print p { margin-bottom: 4px; }

  .slogans { position: absolute; left: 22px; top: 510px; font-family: "Caveat", cursive; font-size: 17px; color: var(--ink); line-height: 1; }
  .slogans p { margin-bottom: 18px; }
  .slogans .indent { padding-left: 28px; }
  .slogans .closing { font-size: 14px; }
</style>
</head>
<body>
<div class="canvas">

  <!-- Outer side: back and front panels -->
  <section class="spread spread--outer">
    <div class="lake-map" role="img" aria-label="Karte des Bodensees"></div>
    <svg class="waves waves--top" viewBox="0 0 520 120" preserveAspectRatio="none" aria-hidden="true">
      <path d="M0 0 H520 V50 C460 50 400 30 330 40 C260 50 200 60 150 55 C110 50 70 60 40 62 C20 63 5 60 0 58 Z" fill="var(--orange)"/>
      <path d="M80 0 H520 V25 C450 20 380 15 300 25 C220 35 170 42 130 30 C100 20 85 10 80 0 Z" fill="var(--orange-dark)" opacity="0.8"/>
      <path d="M10 0 C15 30 40 55 80 58 C120 60 150 50 160 40 L160 0 Z" fill="var(--orange-light)" opacity="0.6"/>
    </svg>
    <svg class="waves waves--bottom" viewBox="0 0 520 90" preserveAspectRatio="none" aria-hidden="true">
      <path d="M0 30 C80 20 180 30 260 40 C330 48 400 20 460 25 C500 28 515 40 520 55 V90 H0 Z" fill="var(--orange)"/>
      <path d="M0 55 C100 60 200 65 300 60 C380 55 420 45 470 60 L480 90 H0 Z" fill="var(--orange-dark)" opacity="0.55"/>
    </svg>
    <div class="fold"></div>

    <div class="panel panel--left">
      <div class="section-tab" style="left:8px; top:132px; width:175px;">Heißgetränke</div>
      <div class="menu-box" style="left:8px; top:154px; width:230px;">
        <div class="menu-item"><span class="menu-item__no">00.</span><div class="menu-item__line">Beispiel Softdrink<span class="menu-item__dots"></span><span class="menu-item__price">0,00€</span></div><span class="menu-item__detail">Beispieldetail</span></div>
        <div class="menu-item"><span class="menu-item__no">00.</span><div class="menu-item__line">Beispiel Softdrink<span class="menu-item__dots"></span><span class="menu-item__price">0,00€</span></div><span class="menu-item__detail">Beispieldetail</span></div>
        <div class="menu-item"><span class="menu-item__no">00.</span><div class="menu-item__line">Beispiel Softdrink<span class="menu-item__dots"></span><span class="menu-item__price">0,00€</span></div><span class="menu-item__detail">Beispieldetail</span></div>
        <div class="menu-item"><span class="menu-item__no">00.</span><div class="menu-item__line">Beispiel Softdrink<span class="menu-item__dots"></span><span class="menu-item__price">0,00€</span></div><span class="menu-item__detail">Beispieldetail</span></div>
        <div class="menu-item"><span class="menu-item__no">00.</span><div class="menu-item__line">Beispiel Softdrink<span class="menu-item__dots"></span><span class="menu-item__price">0,00€</span></div><span class="menu-item__detail">Beispieldetail</span></div>
        <div class="menu-item"><span class="menu-item__no">00.</span><div class="menu-item__line">Beispiel Softdrink<span class="menu-item__dots"></span><span class="menu-item__price">0,00€</span></div><span class="menu-item__detail">Beispieldetail</span></div>
      </div>

      <div class="hours">
        <div class="hours__title">Öffnungszeiten</div>
        <div class="hours__note">Mittwoch Ruhetag</div>
        <div class="hours__block"><span class="hours__day">Montag - Samstag</span><br>10:00 - 23:00 Uhr</div>
        <div class="hours__block"><span class="hours__day">Montag - Freitag</span><br>zwischen 15:00 - 17:00</div>
        <div class="hours__block"><span class="hours__day">Sonntag</span> 14:00 - 22:00 Uhr<br><span class="hours__day">an Feiertagen</span> 14:00 - 23:00 Uhr</div>
      </div>

      <div class="fine-print">
        <p>Schinken = Vorderschinken<br>1.) Farbstoffe; 2.) Konservierungsstoff; 3.) Nitritpökelsalz und Nitrat; 4.) Antioxidationsmittel;<br>5.) Geschmacksverstärker; 6.) Süßstoffe; 7.) geschwärzt; 10.) Phosphat; 11.) koffeinhaltig<br>*Würstchen = gemischt aus Puten- u. Schweinefleisch</p>
        <p>A1.) Weizenmehl; B.) Krebstiere; C.) Eier; D.) Fisch; E.) Milchprodukte;<br>I.) Sellerie Gewürzmischung; N.) Weichtiere Muscheln, Tintenfisch</p>
        <p>Alle Preise in Euro, Preisänderungen, Druckfehler und Irrtümer vorbehalten<br>Stand Januar 2020 - mit dieser Karte verlieren alle anderen Karten ihre Gültigkeit</p>
      </div>
    </div>

    <div class="panel panel--right">
      <div class="slogans">
        <p>Original &amp; Regional</p>
        <p>Heimat des guten geschmacks</p>
        <p>Das Herz, die Seele &amp;<br><span class="indent">der Geschmack des Bodensees</span></p>
        <p class="closing">Aus Liebe zum Bodensee, aus Liebe zur Region</p>
      </div>
    </div>
  </section>

  <!-- Inner side: dishes and drinks -->
  <section class="spread spread--inner">
    <svg class="waves waves--top" viewBox="0 0 520 120" preserveAspectRatio="none" aria-hidden="true">
      <path d="M0 0 H520 V20 C510 60 480 80 430 78 C380 75 330 60 260 58 C190 55 100 40 0 30 Z" fill="var(--orange)"/>
      <path d="M0 0 H480 C470 30 440 40 400 38 C340 35 300 30 260 28 C180 22 100 10 0 15 Z" fill="var(--orange-dark)" opacity="0.6"/>
      <path d="M0 35 C100 45 180 60 260 65 L260 50 C180 45 100 30 0 25 Z" fill="var(--orange-light)" opacity="0.6"/>
    </svg>
    <svg class="waves waves--bottom" viewBox="0 0 520 90" preserveAspectRatio="none" aria-hidden="true">
      <path d="M20 90 C40 50 90 25 150 25 C210 25 240 45 260 50 C340 45 430 40 520 45 V90 Z" fill="var(--orange)"/>
      <path d="M100 90 C130 60 180 45 230 50 C250 52 258 58 260 60 C340 62 430 60 520 65 V90 Z" fill="var(--orange-dark)" opacity="0.5"/>
    </svg>
    <div class="fold"></div>

    <div class="panel panel--left">
      <div class="section-tab" style="left:8px; top:96px; width:215px;">Gerichte</div>
      <div class="menu-box menu-box--dishes" style="left:8px; top:118px; width:240px;">
        <div class="menu-item"><span class="menu-item__no">00.</span><div class="menu-item__line">Beispiel Gericht<span class="menu-item__dots"></span><span class="menu-item__price">0,00€</span></div><span class="menu-item__detail">Schinken<sup>2,5,10</sup>, Gouda<sup>G</sup> und Salami</span></div>
        <div class="menu-item"><span class="menu-item__no">00.</span><div class="menu-item__line">Beispiel Gericht<span class="menu-item__dots"></span><span class="menu-item__price">0,00€</span></div><span class="menu-item__detail">Schinken<sup>2,5,10</sup>, Gouda<sup>G</sup> und Salami</span></div>
        <div class="menu-item"><span class="menu-item__no">00.</span><div class="menu-item__line">Beispiel Gericht<span class="menu-item__dots"></span><span class="menu-item__price">0,00€</span></div><span class="menu-item__detail">Schinken<sup>2,5,10</sup>, Gouda<sup>G</sup> und Salami</span></div>
        <div class="menu-item"><span class="menu-item__no">00.</span><div class="menu-item__line">Beispiel Gericht<span class="menu-item__dots"></span><span class="menu-item__price">0,00€</span></div><span class="menu-item__detail">Schinken<sup>2,5,10</sup>, Gouda<sup>G</sup> und Salami</span></div>
        <div class="menu-item"><span class="menu-item__no">00.</span><div class="menu-item__line">Beispiel Gericht<span class="menu-item__dots"></span><span class="menu-item__price">0,00€</span></div><span class="menu-item__detail">Schinken<sup>2,5,10</sup>, Gouda<sup>G</sup> und Salami</span></div>
        <div class="menu-item"><span class="menu-item__no">00.</span><div class="menu-item__line">Beispiel Gericht<span class="menu-item__dots"></span><span class="menu-item__price">0,00€</span></div><span class="menu-item__detail">Schinken<sup>2,5,10</sup>, Gouda<sup>G</sup> und Salami</span></div>
        <div class="menu-item"><span class="menu-item__no">00.</span><div class="menu-item__line">Beispiel Gericht<span class="menu-item__dots"></span><span class="menu-item__price">0,00€</span></div><span class="menu-item__detail">Schinken<sup>2,5,10</sup>, Gouda<sup>G</sup> und Salami</span></div>
        <div class="menu-item"><span class="menu-item__no">00.</span><div class="menu-item__line">Beispiel Gericht<span class="menu-item__dots"></span><span class="menu-item__price">0,00€</span></div><span class="menu-item__detail">Schinken<sup>2,5,10</sup>, Gouda<sup>G</sup> und Salami</span></div>
        <div class="menu-item"><span class="menu-item__no">00.</span><div class="menu-item__line">Beispiel Gericht<span class="menu-item__dots"></span><span class="menu-item__price">0,00€</span></div><span class="menu-item__detail">Schinken<sup>2,5,10</sup>, Gouda<sup>G</sup> und Salami</span></div>
        <div class="menu-item"><span class="menu-item__no">00.</span><div class="menu-item__line">Beispiel Gericht<span class="menu-item__dots"></span><span class="menu-item__price">0,00€</span></div><span class="menu-item__detail">Schinken<sup>2,5,10</sup>, Gouda<sup>G</sup> und Salami</span></div>
        <div class="menu-item"><span class="menu-item__no">00.</span><div class="menu-item__line">Beispiel Gericht<span class="menu-item__dots"></span><span class="menu-item__price">0,00€</span></div><span class="menu-item__detail">Schinken<sup>2,5,10</sup>, Gouda<sup>G</sup> und Salami</span></div>
        <div class="menu-item"><span class="menu-item__no">00.</span><div class="menu-item__line">Beispiel Gericht<span class="menu-item__dots"></span><span class="menu-item__price">0,00€</span></div><span class="menu-item__detail">Schinken<sup>2,5,10</sup>, Gouda<sup>G</sup> und Salami</span></div>
        <div class="menu-item"><span class="menu-item__no">00.</span><div class="menu-item__line">Beispiel Gericht<span class="menu-item__dots"></span><span class="menu-item__price">0,00€</span></div><span class="menu-item__detail">Schinken<sup>2,5,10</sup>, Gouda<sup>G</sup> und Salami</span></div>
        <div class="menu-item"><span class="menu-item__no">00.</span><div class="menu-item__line">Beispiel Gericht<span class="menu-item__dots"></span><span class="menu-item__price">0,00€</span></div><span class="menu-item__detail">Schinken<sup>2,5,10</sup>, Gouda<sup>G</sup> und Salami</span></div>
        <div class="menu-item"><span class="menu-item__no">00.</span><div class="menu-item__line">Beispiel Gericht<span class="menu-item__dots"></span><span class="menu-item__price">0,00€</span></div><span class="menu-item__detail">Schinken<sup>2,5,10</sup>, Gouda<sup>G</sup> und Salami</span></div>
      </div>
    </div>

    <div class="panel panel--right">
      <div class="section-tab section-tab--right" style="left:28px; top:126px; width:220px;">Biere</div>
      <div class="menu-box" style="left:10px; top:148px; width:240px;">
        <div class="menu-item"><span class="menu-item__no">00.</span><div class="menu-item__line">Beispiel Bier<span class="menu-item__dots"></span><span class="menu-item__price">0,00€</span></div><span class="menu-item__detail">Beispieldetail</span></div>
        <div class="menu-item"><span class="menu-item__no">00.</span><div class="menu-item__line">Beispiel Bier<span class="menu-item__dots"></span><span class="menu-item__price">0,00€</span></div><span class="menu-item__detail">Beispieldetail</span></div>
        <div class="menu-item"><span class="menu-item__no">00.</span><div class="menu-item__line">Beispiel Bier<span class="menu-item__dots"></span><span class="menu-item__price">0,00€</span></div><span class="menu-item__detail">Beispieldetail</span></div>
        <div class="menu-item"><span class="menu-item__no">00.</span><div class="menu-item__line">Beispiel Bier<span class="menu-item__dots"></span><span class="menu-item__price">0,00€</span></div><span class="menu-item__detail">Beispieldetail</span></div>
        <div class="menu-item"><span class="menu-item__no">00.</span><div class="menu-item__line">Beispiel Bier<span class="menu-item__dots"></span><span class="menu-item__price">0,00€</span></div><span class="menu-item__detail">Beispieldetail</span></div>
        <div class="menu-item"><span class="menu-item__no">00.</span><div class="menu-item__line">Beispiel Bier<span class="menu-item__dots"></span><span class="menu-item__price">0,00€</span></div><span class="menu-item__detail">Beispieldetail</span></div>
      </div>

      <div class="section-tab section-tab--right" style="left:28px; top:432px; width:220px;">Softdrinks</div>
      <div class="menu-box" style="left:10px; top:454px; width:240px;">
        <div class="menu-item"><span class="menu-item__no">00.</span><div class="menu-item__line">Beispiel Softdrink<span class="menu-item__dots"></span><span class="menu-item__price">0,00€</span></div><span class="menu-item__detail">Beispieldetail</span></div>
        <div class="menu-item"><span class="menu-item__no">00.</span><div class="menu-item__line">Beispiel Softdrink<span class="menu-item__dots"></span><span class="menu-item__price">0,00€</span></div><span class="menu-item__detail">Beispieldetail</span></div>
        <div class="menu-item"><span class="menu-item__no">00.</span><div class="menu-item__line">Beispiel Softdrink<span class="menu-item__dots"></span><span class="menu-item__price">0,00€</span></div><span class="menu-item__detail">Beispieldetail</span></div>
        <div class="menu-item"><span class="menu-item__no">00.</span><div class="menu-item__line">Beispiel Softdrink<span class="menu-item__dots"></span><span class="menu-item__price">0,00€</span></div><span class="menu-item__detail">Beispieldetail</span></div>
        <div class="menu-item"><span class="menu-item__no">00.</span><div class="menu-item__line">Beispiel Softdrink<span class="menu-item__dots"></span><span class="menu-item__price">0,00€</span></div><span class="menu-item__detail">Beispieldetail</span></div>
        <div class="menu-item"><span class="menu-item__no">00.</span><div class="menu-item__line">Beispiel Softdrink<span class="menu-item__dots"></span><span class="menu-item__price">0,00€</span></div><span class="menu-item__detail">Beispieldetail</span></div>
      </div>
    </div>
  </section>

</div>
</body>
</html>
```